Group of 4 companies needs a new brochure.

We need a brochure design for a group of 4 companies that basically offer financial services based in Dubai, UAE. The 4 companies are 1) debt collection 2) auditing and accounting 3) arbitration and legal experts 4) real estate management. We have old content that could guide you and we want each company in the group to be a standalone A4 brochure with all 4 going in a sleeve. Design for all 4 needs to be uniform, going with our logos colors and i would like it to have a modern arabesque feel something modern and geometric but with a hint of arabesque. I want it to position us as a modern innovative company that people want to be associated with. One logo is attached to give an idea of our colors.
Update 1: The Logos and Profiles content have been uploaded please use www.velmo-grp.ae as a reference or for further content.
Please do not include the entire content i uploaded, summarize the important bits.
Update 2: You can join Velmo auditing and Velmo financial consultancy as one brouchure as they have similar activities
If you have any questions do not hesitate to ask!
All the files have been uploaded, if you have any questions do not hesitate to ask!
1. The budget has been increased!
2. You can use our website www.velmo-grp.ae for more information including contacts, location and more information you may need on our operations.
Dear Designers,
There is some confusion regarding the requirements, to clarify, i have posted an image of the folder/brochure to give you an idea of what to do.
Requirement:
1) 1 A4 Folder- Velmo Group logo and contacts/location to put brochures in (see the uploaded picture for an idea of what the folder should look like)
2) 1 A4 Brochure - Velmo Debt Collection
3) 1 A4 Brochure - Velmo Financial Consultants and Velmo Auditing
4) 1 A4 Brochure - Velmo Real Estate Brokers
Further, i will be monitoring the submissions and your comments and i am willing to double the budget if i see the requirements are being met.
Do not hesitate to contact me for any further inquiries or comments.
Thank you!
Dear Designers, i have taken your comments into consideration and guaranteed the payment.
B2b, banks, financial institutions, large companies
Real Estate

```html
<!DOCTYPE html>
<html lang="en">
<head>
<meta charset="utf-8">
<title>Velmo Group – Trifold Brochure</title>
<link rel="stylesheet" href="https://fonts.googleapis.com/css2?family=Cinzel+Decorative:wght@400;700&family=Lato:wght@400;700&family=Oswald:wght@700&display=swap">
<style>
  :root {
    --canvas: #e8ebf0;
    --navy: #1f2a8c;
    --navy-deep: #1a226e;
    --ink: #18204a;
    --white: #ffffff;
  }
  * { margin: 0; padding: 0; box-sizing: border-box; }
  html, body { width: 1200px; height: 900px; overflow: hidden; background: var(--canvas); }
  .brochure {
    position: absolute; left: 99px; top: 93px;
    width: 1002px; height: 713px;
    overflow: hidden;
    box-shadow: 0 6px 18px rgba(20, 30, 80, .25);
  }
  .brochure__art { position: absolute; inset: 0; }
  .section-pill {
    position: absolute; left: 5px; height: 30px;
    padding: 0 20px 0 16px; border-radius: 0 16px 16px 0;
    background: var(--navy-deep); color: var(--white);
    font: 700 13px/30px "Cinzel Decorative", serif; letter-spacing: .3px;
  }
  .section-body {
    position: absolute; left: 21px; width: 300px;
    font: 400 12.2px/15.4px "Lato", sans-serif; color: var(--ink);
  }
  .group-title {
    position: absolute; left: 358px; top: 346px;
    font: 700 18px/1 "Cinzel Decorative", serif; color: var(--navy);
  }
  .contact-list { position: absolute; left: 380px; top: 385px; list-style: none; }
  .contact-list li {
    display: flex; align-items: flex-start; gap: 9px;
    font: 700 13.4px/17px "Lato", sans-serif; color: var(--navy-deep);
    margin-bottom: 6px;
  }
  .contact-list svg { flex: 0 0 13px; width: 13px; height: 13px; margin-top: 2px; fill: var(--white); }
  .brand-name {
    position: absolute; left: 690px; top: 398px; width: 300px; text-align: center;
    white-space: nowrap;
    font: 700 50px/1 "Oswald", sans-serif; color: var(--navy); letter-spacing: 1px;
  }
  .tagline { position: absolute; left: 694px; top: 532px; font-family: "Cinzel Decorative", serif; white-space: nowrap; }
  .tagline span { display: block; font-weight: 700; }
  .tagline__lead { font-size: 24px; line-height: 32px; color: var(--navy-deep); }
  .tagline__second { font-size: 19.5px; line-height: 28px; color: var(--navy-deep); }
  .tagline__small { font-size: 14.5px; line-height: 22px; color: var(--white); }
</style>
</head>
<body>
<main class="brochure">
  <svg class="brochure__art" viewBox="0 0 1002 713" width="1002" height="713">
    <defs>
      <linearGradient id="leftPanel" x1="0" x2="1"><stop offset="0" stop-color="#3b79cc"/><stop offset="1" stop-color="#5b9ae2"/></linearGradient>
      <linearGradient id="midPanel" x1="0" x2="1"><stop offset="0" stop-color="#86bdf2"/><stop offset="1" stop-color="#5a98e0"/></linearGradient>
      <linearGradient id="rightPanel" x1="0" x2="1"><stop offset="0" stop-color="#7cb4ee"/><stop offset="1" stop-color="#3f7fd0"/></linearGradient>
      <linearGradient id="photoTone" x1="0" x2="1" y1="0" y2="1"><stop offset="0" stop-color="#dfe3ea"/><stop offset=".55" stop-color="#d9a98c"/><stop offset="1" stop-color="#b98469"/></linearGradient>
      <linearGradient id="waveNavy" x1="0" x2="1"><stop offset="0" stop-color="#24309a"/><stop offset="1" stop-color="#1a2273"/></linearGradient>
    </defs>
    <rect class="panel panel--left" x="0" y="0" width="340" height="713" fill="url(#leftPanel)"/>
    <rect class="panel panel--middle" x="340" y="0" width="332" height="713" fill="url(#midPanel)"/>
    <rect class="panel panel--right" x="672" y="0" width="330" height="713" fill="url(#rightPanel)"/>
    <path class="photo-frame" role="img" aria-label="Photo: an open hand holding house keys on a key ring above paperwork"
      d="M478,0 C466,40 500,72 480,112 C458,160 470,222 502,244 C540,270 566,292 604,302 C652,314 690,346 722,356 C782,372 852,340 902,312 C950,286 988,272 1002,264 L1002,0 Z"
      fill="url(#photoTone)" stroke="#ffffff" stroke-width="4"/>
    <path d="M472,0 C460,40 494,72 474,112 C452,160 464,226 498,250 C536,276 562,298 600,308 C650,320 688,352 722,362 C784,378 856,346 906,318 C952,292 990,280 1002,272"
      fill="none" stroke="#1f2a8c" stroke-width="3"/>
    <path class="wave wave--bottom"
      d="M0,470 C80,445 180,445 260,470 C360,505 440,585 560,620 C660,650 780,662 885,668 L885,713 L0,713 Z"
      fill="url(#waveNavy)"/>
    <path d="M0,470 C80,445 180,445 260,470 C360,505 440,585 560,620 C660,650 780,662 885,668"
      fill="none" stroke="#ffffff" stroke-width="3"/>
    <path class="wave wave--corner" d="M555,640 C720,705 990,710 1002,505 L1002,713 L555,713 Z" fill="url(#waveNavy)"/>
    <path d="M555,640 C720,705 990,710 1002,505" fill="none" stroke="#ffffff" stroke-width="4"/>
    <path d="M600,660 C760,712 985,715 1002,565" fill="none" stroke="#ffffff" stroke-width="2" opacity=".7"/>
  </svg>

  <h2 class="section-pill" style="top:35px">Quality Assurance</h2>
  <p class="section-body" style="top:72px">
    Velmo Debt collections are ensuring the following steps to maintain the quality of the clients<br>
    • Hiring collectors with proven record in collections.<br>
    • Call monitoring system.<br>
    • Collector training on etiquettes of calling as per client defined procedures.<br>
    • Managing bank records with backup servers and saving data and work on timely basis
  </p>

  <h2 class="section-pill" style="top:213px">About Velmo</h2>
  <p class="section-body" style="top:254px">
    VELMO is a team of professionals, engaged in providing a high quality services to our valuable clients, in order to meet their business requirements, especially in financial &amp; business sector. The Company works as an intermediary between the clients and their stakeholders with a most efficient and cost-effective way of prioritizing the business needs. We have tremendously developed integrated network of searching, repossessing, collecting, recovering &amp; surveying of assets &amp; others in UAE with addition to our intercity self-relations with the Govt. authorities.
  </p>

  <h3 class="group-title">Velmo Group of Companies</h3>
  <ul class="contact-list">
    <li><svg viewBox="0 0 16 16"><path d="M8 1 1 7.5h2V15h4v-4h2v4h4V7.5h2z"/></svg><span>210 Al Sahel Bldg Qusais Palm Street<br>OPP, Noura Driving School</span></li>
    <li><svg viewBox="0 0 16 16"><path d="M1 3h14v10H1zM2 4l6 5 6-5"/></svg><span>info@velmodebtcollection.com</span></li>
    <li><svg viewBox="0 0 16 16"><circle cx="8" cy="8" r="7"/></svg><span>www.velmo-grp.ae</span></li>
    <li><svg viewBox="0 0 16 16"><path d="M3 1h3l1.5 4-2 1.3a9 9 0 0 0 4.2 4.2l1.3-2 4 1.5v3c0 1-1 2-2 2C7 15 1 9 1 3c0-1 1-2 2-2z"/></svg><span>045550142</span></li>
    <li><svg viewBox="0 0 16 16"><path d="M1 6c4-4 10-4 14 0l-2 2-2.5-1V5a9 9 0 0 0-5 0v2L3 8zM4 9h8l1 6H3z"/></svg><span>045550187</span></li>
  </ul>

  <div class="brand-name">VELMO GROUP</div>

  <p class="tagline">
    <span class="tagline__lead">We aim to become</span>
    <span class="tagline__second">a creative company</span>
    <span class="tagline__small">that grows continuously</span>
    <span class="tagline__small">throughout the future</span>
  </p>
</main>
</body>
</html>
```